Business Card Design - Corporate

Create a sleek elegant business card layout while suggesting a color scheme. Convey cutting edge technology while maintaining a corporate feel that is easily readable.

Company designs and manufactures consumer electronic products for mass retail that are mainly app driven.

(vector logo and die-line provided)

Target Market(s)

Corporate level, tech industry.

Industry/Entity Type

Business

Contact Information for Business Card

Generic Info:

Name
Title
email
address
phone 1
phone 2
website (quillbarn.com) on back

Font styles to use
Sans Serif

Requirements
Must have
• At least 2 colors + white on one side.
Nice to have
• Solid suggestion on color for logo and overall design. Color flood on back of card.
Should not have
• background texture like... marble, stone, patterns or circuit boards

```html
<!DOCTYPE html>
<html lang="en">
<head>
<meta charset="utf-8">
<title>Quillbarn Business Card</title>
<link rel="stylesheet" href="https://fonts.googleapis.com/css2?family=Ubuntu:wght@300;400;500;700&display=swap">
<style>
  :root {
    --stage: #e4e4e4;
    --card-dark: #58585b;
    --card-light: #f2f2f0;
    --ink: #3d3d40;
    --ink-soft: #4a4a4d;
    --accent: #1b70c4;
    --logo-on-dark: #3a3a3c;
  }
  * { margin: 0; padding: 0; box-sizing: border-box; }
  html, body {
    width: 1200px;
    height: 1200px;
    overflow: hidden;
    background: var(--stage);
    font-family: "Ubuntu", sans-serif;
  }
  .canvas {
    position: relative;
    width: 1200px;
    height: 1200px;
  }
  .card {
    position: absolute;
    left: 160px;
    width: 880px;
    height: 500px;
    border-radius: 4px;
    box-shadow: 0 6px 18px rgba(0,0,0,0.18);
    overflow: hidden;
  }
  .card--back {
    top: 60px;
    background: var(--card-dark);
    display: flex;
    align-items: center;
    justify-content: center;
  }
  .card--back .wordmark {
    color: var(--logo-on-dark);
    font-size: 64px;
    letter-spacing: 10px;
  }
  .card--front {
    top: 640px;
    background: var(--card-light);
    color: var(--ink);
  }
  .wordmark {
    font-family: "Ubuntu", sans-serif;
    font-weight: 300;
    text-transform: uppercase;
    line-height: 1;
  }
  .front-art {
    position: absolute;
    top: 0;
    right: 0;
    width: 420px;
    height: 330px;
  }
  .card--front .wordmark {
    position: absolute;
    left: 60px;
    top: 80px;
    color: var(--ink);
    font-size: 62px;
    letter-spacing: 9px;
  }
  .identity {
    position: absolute;
    left: 60px;
    top: 230px;
  }
  .identity__name {
    color: var(--accent);
    font-size: 34px;
    font-weight: 500;
    letter-spacing: 1px;
  }
  .identity__title {
    margin-top: 6px;
    font-size: 22px;
    font-weight: 300;
    color: var(--ink-soft);
  }
  .identity__address {
    position: absolute;
    left: 280px;
    top: 275px;
    font-size: 22px;
    font-weight: 300;
    color: var(--ink-soft);
  }
  .rule {
    position: absolute;
    left: 60px;
    right: 90px;
    top: 320px;
    height: 2px;
    background: var(--accent);
  }
  .contacts {
    position: absolute;
    left: 60px;
    top: 345px;
    display: flex;
    font-size: 21px;
    font-weight: 300;
    color: var(--ink-soft);
  }
  .contacts__col {
    display: flex;
    flex-direction: column;
    gap: 10px;
    padding-right: 22px;
  }
  .contacts__col + .contacts__col {
    padding-left: 22px;
    border-left: 2px solid var(--accent);
  }
  .contacts__label {
    display: inline-block;
    width: 40px;
    color: var(--accent);
    font-weight: 700;
  }
</style>
</head>
<body>
<main class="canvas">
  <section class="card card--back" aria-label="Card back">
    <span class="wordmark">Quillbarn</span>
  </section>

  <section class="card card--front" aria-label="Card front">
    <svg class="front-art" viewBox="0 0 420 330" role="img" aria-label="Rocket illustration in dark grey across the top right corner">
      <path d="M0 0 H420 V330 C360 250 270 160 150 95 C90 62 40 40 0 30 Z" fill="var(--card-dark)"/>
    </svg>

    <span class="wordmark">Quillbarn</span>

    <div class="identity">
      <p class="identity__name">JOHN DOE</p>
      <p class="identity__title">Director</p>
    </div>
    <p class="identity__address">Dummy city, Dummy country land</p>

    <div class="rule"></div>

    <div class="contacts">
      <div class="contacts__col">
        <span><span class="contacts__label">T :</span>123-456-7890</span>
        <span><span class="contacts__label">F :</span>123-456-7890</span>
      </div>
      <div class="contacts__col">
        <span><span class="contacts__label">W :</span>www.quillbarn.com</span>
        <span><span class="contacts__label">E :</span>john@quillbarn.com</span>
      </div>
    </div>
  </section>
</main>
</body>
</html>
```